Banners for slider on first page of the website

We need up to 3 different banners for our website: www.trelk.si
Current design is maybe a bit too playful, so do not mind on it. It can include some natural elements
1) Design needs to be modern type
2) Has to include products which are on our website
3) Has to be in two sizes: mobile and web - like we have now
4) Each slider CAN represent each category we have or CAN include multiple
5) Optional text holders

```html
<!DOCTYPE html>
<html lang="sl">
<head>
<meta charset="utf-8">
<title>Kopalne bombice – slider</title>
<link rel="stylesheet" href="https://fonts.googleapis.com/css2?family=Open+Sans:wght@400&family=Poppins:wght@600&display=swap">
<style>
  :root{
    --panel-light:#fdeef4;
    --panel-mid:#fbdbe7;
    --band-pink:#f7b9cf;
    --band-soft:#fbd3e1;
    --accent-pink:#df6c8e;
    --text-grey:#77757a;
    --ribbon:#f68aae;
    --white:#ffffff;
    --photo-light:#ebe7e8;
    --photo-mid:#dcd5d7;
    --photo-blush:#e9c7d0;
  }
  html,body{margin:0;padding:0;overflow:hidden;}
  body{width:1200px;height:466px;background:var(--white);}
  .banner{position:relative;width:1200px;height:466px;overflow:hidden;
    background:linear-gradient(100deg,var(--panel-mid) 0%,var(--panel-light) 40%,var(--panel-mid) 100%);}
  .banner__illustration{position:absolute;left:60px;top:10px;width:640px;height:430px;
    border-radius:50%;background:radial-gradient(ellipse,rgba(255,255,255,.35),transparent 70%);}
  .banner__photo{position:absolute;inset:0;
    clip-path:polygon(869px 0,1200px 0,1200px 466px,706px 466px);
    background:linear-gradient(160deg,var(--photo-light) 0%,var(--photo-blush) 45%,var(--photo-mid) 100%);}
  .banner__bands{position:absolute;inset:0;width:1200px;height:466px;}
  .banner__copy{position:absolute;left:97px;top:82px;font-family:"Open Sans",sans-serif;}
  .banner__kicker{margin:0;font-weight:400;font-size:30.5px;letter-spacing:-0.4px;color:var(--text-grey);line-height:1;}
  .banner__title{margin:0;margin-top:12px;font-weight:400;font-size:96px;line-height:0.97;letter-spacing:-1.2px;}
  .banner__title-top{display:block;color:var(--accent-pink);}
  .banner__title-bottom{display:block;color:var(--text-grey);}
  .banner__cta{position:absolute;left:85px;top:343px;width:350px;height:70px;text-decoration:none;}
  .banner__cta-label{position:absolute;inset:0;display:flex;align-items:center;justify-content:center;
    font-family:"Poppins",sans-serif;font-weight:600;font-size:20.5px;color:var(--white);letter-spacing:-0.3px;padding-left:8px;}
</style>
</head>
<body>
  <section class="banner">
    <div class="banner__illustration" role="img" aria-label="Faint illustration of a bathtub with bubbles"></div>
    <div class="banner__photo" role="img" aria-label="Product photo of pink and white bath bombs with rose petals"></div>
    <svg class="banner__bands" viewBox="0 0 1200 466" aria-hidden="true">
      <polygon points="788,0 869,0 706,466 663,466" fill="var(--band-pink)"/>
      <polygon points="800,0 812,0 680,466 668,466" fill="var(--band-soft)"/>
      <polygon points="0,0 60,0 0,170" fill="var(--band-soft)" opacity=".7"/>
    </svg>
    <div class="banner__copy">
      <p class="banner__kicker">OGLEJ SI PONUDBO</p>
      <h1 class="banner__title">
        <span class="banner__title-top">KOPALNE</span>
        <span class="banner__title-bottom">BOMBICE</span>
      </h1>
    </div>
    <a class="banner__cta" href="#">
      <svg viewBox="0 0 350 70" width="350" height="70" aria-hidden="true">
        <polygon points="0,0 350,0 322,35 350,70 0,70 28,35" fill="var(--ribbon)" opacity=".92"/>
      </svg>
      <span class="banner__cta-label">ACHETEZ MAINTENANT</span>
    </a>
  </section>
</body>
</html>
```